Brightwell Pictures Business Card

Hello,

i would like to have a dynamic, creative but tasteful card, colour used, front and back. I have attached a sample card that I liked very much from another individual to give you an idea of the theme/approach, but not colour. Ideally the graphic elements of the Brightwell Logo are brought into the design.

Target Market(s)

North America

Industry/Entity Type

Film Production

Contact Information for Business Card

Mirela Vantasch
President/Founder
Brightwell Pictures Inc.
587 914 3362
mirela@brightwellpix.tv

Font styles to use
Sans Serif

Colors
6b449b
5c5c5c
fdfdfd
000000

Requirements
Must have
• Logo, name, Company name, email and cell number. no Address line to be included.
Should not have
• any unrelated GFX elements, serif fonts

```html
<!DOCTYPE html>
<html lang="en">
<head>
<meta charset="utf-8">
<title>Brightwell Pictures Business Card</title>
<link rel="stylesheet" href="https://fonts.googleapis.com/css2?family=Montserrat:wght@500;600;700;800&display=swap">
<style>
  :root {
    --purple: #5b2d90;
    --grey: #5c5c5c;
    --paper: #fdfdfd;
    --ink: #000000;
    --backdrop: #4b4d4f;
  }
  * { margin: 0; padding: 0; box-sizing: border-box; }
  html, body { width: 800px; height: 1200px; overflow: hidden; }
  body {
    background: var(--backdrop);
    font-family: "Montserrat", sans-serif;
    position: relative;
  }
  .card {
    position: absolute;
    left: 80px;
    width: 640px;
    height: 366px;
    overflow: hidden;
    box-shadow: 0 12px 30px rgba(0,0,0,0.35);
  }
  .card--front { top: 117px; background: var(--purple); }
  .card--back { top: 717px; background: var(--paper); }
  .card svg { position: absolute; inset: 0; }

  .wordmark {
    position: absolute;
    display: flex;
    align-items: center;
    gap: 10px;
    font-weight: 800;
    color: var(--grey);
    letter-spacing: -1px;
  }
  .wordmark__dot {
    border-radius: 50%;
    background: var(--purple);
    flex: none;
  }
  .card--front .wordmark { left: 0; right: 0; top: 150px; justify-content: center; font-size: 56px; }
  .card--front .wordmark__dot { width: 30px; height: 30px; }

  .name-bar {
    position: absolute;
    left: 0; top: 40px;
    width: 300px; height: 40px;
    background: var(--purple);
    border-radius: 0 8px 8px 0;
    color: var(--paper);
    font-weight: 700;
    font-size: 22px;
    line-height: 40px;
    padding-left: 30px;
  }
  .job-title {
    position: absolute;
    left: 30px; top: 88px;
    font-size: 15px; font-weight: 600;
    color: var(--grey);
  }
  .card--back .wordmark { left: 30px; top: 140px; font-size: 48px; }
  .card--back .wordmark__dot { width: 24px; height: 24px; }

  .contact { position: absolute; left: 30px; top: 262px; list-style: none; }
  .contact__item {
    display: flex; align-items: center; gap: 10px;
    font-size: 21px; font-weight: 600; color: var(--grey);
    margin-bottom: 12px;
  }
  .contact__icon {
    width: 30px; height: 30px; border-radius: 50%;
    background: var(--purple);
    display: flex; align-items: center; justify-content: center;
    flex: none;
  }
  .contact__icon svg { position: static; }
  .arc-label {
    font-family: "Montserrat", sans-serif;
    font-weight: 700; font-size: 21px; fill: var(--paper);
  }
</style>
</head>
<body>

<section class="card card--front" aria-label="Card front">
  <svg width="640" height="366" viewBox="0 0 640 366" aria-hidden="true">
    <polygon points="0,258 640,258 640,270 0,270" fill="var(--paper)"/>
    <polygon points="0,96 640,96 640,108 0,108" fill="var(--paper)"/>
    <polygon points="150,108 520,108 560,183 520,258 150,258 110,183" fill="var(--paper)"/>
  </svg>
  <div class="wordmark"><span class="wordmark__dot"></span><span>brightwell</span></div>
</section>

<section class="card card--back" aria-label="Card back">
  <svg width="640" height="366" viewBox="0 0 640 366">
    <defs>
      <path id="ring-path" d="M 378 -20 A 262 262 0 0 0 640 242"/>
    </defs>
    <circle cx="640" cy="-20" r="300" fill="var(--purple)"/>
    <circle cx="640" cy="-20" r="226" fill="var(--paper)"/>
    <circle cx="640" cy="-20" r="210" fill="var(--purple)" role="img" aria-label="Aperture blade motif"/>
    <text class="arc-label" dominant-baseline="middle">
      <textPath href="#ring-path" startOffset="50%" text-anchor="middle">Brightwell Pictures Inc.</textPath>
    </text>
  </svg>

  <div class="name-bar">Mirela Vantasch</div>
  <p class="job-title">President / Founder</p>

  <div class="wordmark"><span>brightwell</span><span class="wordmark__dot"></span></div>

  <ul class="contact">
    <li class="contact__item">
      <span class="contact__icon">
        <svg width="14" height="18" viewBox="0 0 14 18" aria-hidden="true">
          <rect x="1.5" y="1" width="11" height="16" rx="2" fill="none" stroke="var(--paper)" stroke-width="2"/>
          <line x1="5" y1="14" x2="9" y2="14" stroke="var(--paper)" stroke-width="1.6"/>
        </svg>
      </span>
      587 914 3362
    </li>
    <li class="contact__item">
      <span class="contact__icon">
        <svg width="18" height="13" viewBox="0 0 18 13" aria-hidden="true">
          <rect x="1" y="1" width="16" height="11" fill="none" stroke="var(--paper)" stroke-width="1.8"/>
          <polyline points="1,1 9,8 17,1" fill="none" stroke="var(--paper)" stroke-width="1.8"/>
        </svg>
      </span>
      mirela@brightwellpix.tv
    </li>
  </ul>
</section>

</body>
</html>
```